KVT Business Cards

We require business cards for our business. We would like a matte black back to the card, with our logo centred in the middle. The front side of the card is open to design.

Target Market(s)

Clients looking for legal services (professional)

Industry/Entity Type

Legal

Contact Information for Business Card

Boris Telemark
Partner
Mobile: 0438 715 642
Email: boris@kvtlaw.co
Website: www.kvtlaw.co
Level 3, 118 Wexbury Street
Sydney NSW 2000

Font styles to use
Other font styles liked:
• Avenir

Colors
f04a50
ffffff
1b1b1b

Requirements
Must have
• Black back with logo included in the centre of the card.
• Our font is Avenir.

```html
<!DOCTYPE html>
<html lang="en">
<head>
<meta charset="utf-8">
<title>KVT Business Cards</title>
<link href="https://fonts.googleapis.com/css2?family=Nunito+Sans:wght@400;600;700&display=swap" rel="stylesheet">
<style>
  :root {
    --red: #f04a50;
    --white: #ffffff;
    --ink: #1b1b1b;
    --card: #0d0d0d;
    --stage: #3a3631;
    --muted: #d8d8d8;
  }
  * { margin: 0; padding: 0; box-sizing: border-box; }
  html, body { width: 1200px; height: 720px; overflow: hidden; }
  body {
    background: var(--stage);
    font-family: "Nunito Sans", "Avenir", sans-serif;
    position: relative;
  }
  .card {
    position: absolute;
    top: 205px;
    width: 540px;
    height: 309px;
    background: var(--card);
    overflow: hidden;
    box-shadow: 0 10px 30px rgba(0,0,0,0.45);
  }
  .card--front { left: 40px; }
  .card--back { left: 620px; display: flex; align-items: center; justify-content: center; }
  .card__frames { position: absolute; inset: 0; width: 100%; height: 100%; }

  .brand { display: flex; align-items: center; gap: 10px; color: var(--white); font-weight: 700; letter-spacing: 0.06em; }
  .brand__mark { background: var(--red); display: block; }
  .brand--small { position: absolute; left: 32px; top: 44px; font-size: 20px; }
  .brand--small .brand__mark { width: 16px; height: 16px; }
  .brand--large { font-size: 46px; gap: 16px; }
  .brand--large .brand__mark { width: 34px; height: 34px; }

  .person { position: absolute; left: 210px; top: 92px; text-align: center; width: 210px; }
  .person__name { color: var(--red); font-size: 22px; font-weight: 700; line-height: 1.1; }
  .person__role { color: var(--muted); font-size: 18px; font-weight: 400; letter-spacing: 0.04em; }

  .contacts { position: absolute; left: 208px; top: 158px; list-style: none; }
  .contacts__item { display: flex; align-items: flex-start; gap: 12px; color: var(--muted); font-size: 13.5px; line-height: 1.3; margin-bottom: 7px; }
  .contacts__icon { width: 14px; height: 14px; flex: none; margin-top: 2px; fill: var(--red); }
</style>
</head>
<body>
  <section class="card card--front" aria-label="Business card front">
    <svg class="card__frames" viewBox="0 0 540 309" aria-hidden="true">
      <g fill="none" stroke="#f04a50" stroke-linejoin="miter">
        <path d="M438 0 V40 H540" stroke-width="7"/>
        <path d="M456 0 V60 H540" stroke-width="1.5"/>
        <path d="M470 0 V74 H540" stroke-width="1.5"/>
        <path d="M0 196 H132 V309" stroke-width="9"/>
        <path d="M0 178 H112 V309" stroke-width="1.5"/>
        <path d="M0 164 H98 V309" stroke-width="1.5"/>
      </g>
    </svg>

    <div class="brand brand--small">
      <span class="brand__mark"></span>
      <span class="brand__name">KVT</span>
    </div>

    <div class="person">
      <p class="person__name">Boris Telemark</p>
      <p class="person__role">Partner</p>
    </div>

    <ul class="contacts">
      <li class="contacts__item">
        <svg class="contacts__icon" viewBox="0 0 24 24" aria-hidden="true"><path d="M6.6 10.8a15.1 15.1 0 0 0 6.6 6.6l2.2-2.2a1 1 0 0 1 1-.25 11.4 11.4 0 0 0 3.6.57 1 1 0 0 1 1 1V20a1 1 0 0 1-1 1A17 17 0 0 1 3 4a1 1 0 0 1 1-1h3.5a1 1 0 0 1 1 1c0 1.25.2 2.45.57 3.57a1 1 0 0 1-.25 1z"/></svg>
        <span>Mobile: 0438 715 642</span>
      </li>
      <li class="contacts__item">
        <svg class="contacts__icon" viewBox="0 0 24 24" aria-hidden="true"><path d="M2 5h20v14H2z M2 5l10 8 10-8" fill="#f04a50" stroke="#0d0d0d" stroke-width="1.5"/></svg>
        <span>Email: boris@kvtlaw.co</span>
      </li>
      <li class="contacts__item">
        <svg class="contacts__icon" viewBox="0 0 24 24" aria-hidden="true"><g fill="none" stroke="#f04a50" stroke-width="2"><circle cx="12" cy="12" r="9.5"/><ellipse cx="12" cy="12" rx="4" ry="9.5"/><path d="M2.5 12h19M4 7h16M4 17h16"/></g></svg>
        <span>Website: www.kvtlaw.co</span>
      </li>
      <li class="contacts__item">
        <svg class="contacts__icon" viewBox="0 0 24 24" aria-hidden="true"><path d="M12 2a7 7 0 0 0-7 7c0 5 7 13 7 13s7-8 7-13a7 7 0 0 0-7-7zm0 9.5A2.5 2.5 0 1 1 12 6.5a2.5 2.5 0 0 1 0 5z"/></svg>
        <span>Level 3, 118 Wexbury Street<br>Sydney NSW 2000</span>
      </li>
    </ul>
  </section>

  <section class="card card--back" aria-label="Business card back">
    <div class="brand brand--large">
      <span class="brand__mark"></span>
      <span class="brand__name">KVT</span>
    </div>
  </section>
</body>
</html>
```